Dalwin Tasker Construction LLC

I like to have a business card the is unique, very professional and the it will projected the best first impression of me and my company

Target Market(s)

Remodeling, new constitution

Industry/Entity Type

Business

Font styles to use
Script

Requirements
Must have
• My company name email and phone number
Nice to have
• A logo maybe

```html
<!DOCTYPE html>
<html lang="en">
<head>
<meta charset="utf-8">
<title>Dalwin Tasker Construction LLC – Business Card</title>
<link rel="stylesheet" href="https://fonts.googleapis.com/css2?family=Great+Vibes&family=Roboto:wght@400;700&display=swap">
<style>
  :root {
    --stage: #161616;
    --card-dark: #0c0c0c;
    --card-mid: #262626;
    --ink-white: #f4f4f4;
    --accent-red: #e3182b;
    --hazard-yellow: #b7a61e;
    --icon-gold: #c9a227;
  }
  * { box-sizing: border-box; margin: 0; padding: 0; }
  html, body {
    width: 1200px; height: 800px; overflow: hidden;
    background: var(--stage);
  }
  .stage {
    position: relative; width: 1200px; height: 800px;
    display: flex; align-items: center; justify-content: center; gap: 60px;
  }
  .card {
    position: relative; width: 520px; height: 300px; overflow: hidden;
    background: radial-gradient(ellipse at 55% 35%, var(--card-mid) 0%, var(--card-dark) 75%);
    box-shadow: 0 10px 30px rgba(0,0,0,.6);
    color: var(--ink-white);
    font-family: "Roboto", Arial, sans-serif;
  }
  .wordmark { position: absolute; text-align: left; }
  .wordmark__name {
    font-family: "Great Vibes", cursive;
    color: var(--ink-white); line-height: 1; white-space: nowrap;
  }
  .wordmark__sub {
    color: var(--accent-red); font-weight: 700;
    text-transform: uppercase; letter-spacing: .32em; white-space: nowrap;
  }
  /* front */
  .card--front .wordmark { left: 70px; top: 78px; }
  .card--front .wordmark__name { font-size: 76px; }
  .card--front .wordmark__sub { font-size: 17px; margin: 4px 0 0 14px; }
  .hazard-band { position: absolute; left: 0; bottom: 34px; width: 520px; height: 14px; }
  /* back */
  .person { position: absolute; left: 34px; top: 30px; }
  .person__name { font-family: "Great Vibes", cursive; font-size: 30px; line-height: 1; }
  .person__role {
    color: var(--accent-red); font-weight: 700; font-size: 11px;
    letter-spacing: .3em; margin-top: 2px;
  }
  .address {
    position: absolute; left: 34px; top: 128px;
    font-size: 12px; letter-spacing: .18em; line-height: 1.35;
  }
  .card--back .wordmark { right: 30px; top: 110px; text-align: right; }
  .card--back .wordmark__name { font-size: 48px; }
  .card--back .wordmark__sub { font-size: 11px; margin-top: 2px; }
  .contact {
    position: absolute; right: 30px; bottom: 26px; list-style: none;
    font-size: 13px; letter-spacing: .18em; text-align: right;
  }
  .contact li { display: flex; justify-content: flex-end; align-items: center; gap: 8px; line-height: 1.5; }
  .contact svg { width: 12px; height: 12px; flex: none; }
</style>
</head>
<body>
<main class="stage">
  <section class="card card--front">
    <div class="wordmark">
      <div class="wordmark__name">Dalwin Tasker</div>
      <div class="wordmark__sub">Construction LLC</div>
    </div>
    <svg class="hazard-band" viewBox="0 0 520 14" aria-hidden="true">
      <defs>
        <pattern id="hazard" width="20" height="14" patternUnits="userSpaceOnUse">
          <rect x="2" y="1" width="11" height="12" fill="var(--hazard-yellow)"/>
        </pattern>
      </defs>
      <rect width="520" height="14" fill="url(#hazard)"/>
    </svg>
  </section>

  <section class="card card--back">
    <div class="person">
      <div class="person__name">Marcus Bell</div>
      <div class="person__role">MANAGER</div>
    </div>
    <address class="address" style="font-style:normal">
      418 Harbor Street<br>Brookfield 30417
    </address>
    <div class="wordmark">
      <div class="wordmark__name">Dalwin Tasker</div>
      <div class="wordmark__sub">Construction LLC</div>
    </div>
    <ul class="contact">
      <li>2468 1357 9024
        <svg viewBox="0 0 12 12" aria-label="phone"><path d="M2 1h3l1 3-2 1a7 7 0 0 0 3 3l1-2 3 1v3c-6 0-10-4-10-9z" fill="var(--icon-gold)"/></svg>
      </li>
      <li>marcus@daltasker.com
        <svg viewBox="0 0 12 12" aria-label="email"><rect x="0.5" y="2" width="11" height="8" fill="var(--icon-gold)"/><path d="M1 2.5l5 4 5-4" stroke="#111" fill="none"/></svg>
      </li>
      <li>www.daltasker.com
        <svg viewBox="0 0 12 12" aria-label="website"><rect x="1" y="1.5" width="10" height="7" fill="none" stroke="var(--icon-gold)" stroke-width="1.4"/><rect x="4" y="9.5" width="4" height="1.5" fill="var(--icon-gold)"/></svg>
      </li>
    </ul>
  </section>
</main>
</body>
</html>
```